Fahrzeugbeschriftung für Darmtherapie und Kurspraxis
Zielgruppe
Kurspraxis Sonnenfunken Kelbach. die Kurspraxis, Workshops, (siehe Flyer). und holistische Darmtherapie heiter vital petra lohmann
Diese Beklebung soll dazu dienen, die Reichweite von Sonnenfunken Kelbach und Heiter vital zu erhöhen und potenzielle Kunden auf die Dienstleistungen aufmerksam zu machen.
sonnenfunken: https://www.sonnenfunken-kelbach.de
Adresse:** Talwiesenweg 48, Oberhausen
Beschreibung: sonnenfunken ist ein Ort, der Familien verbindet. Das Unternehmen bietet ein breites Spektrum an Kursen für alle Altersgruppen an, von Schwimmkursen über Yoga bis hin zu Rückbildungskursen. Darüber hinaus bietet sonnenfunken einen Ort des Austauschs und eine Gemeinschaft für Gleichgesinnte.
- Heiter vital Petra Lohmann: Darmtherapie für Frauen, Mamas und Frauen mit Kinderwunsch: https://www.heiter-vital-petra-lohmann.de
-Beschreibung: Petra Lohmann bietet eine Darmtherapie an, die darauf abzielt, das Immunsystem ganzheitlich zu regulieren und bei hormonellem Ungleichgewicht zu helfen. Diese Therapie ist auch für Babys und Kinder geeignet und kann zu mehr Kraft, reguliertem Hormonhaushalt und einem neuen Lebensgefühl führen.
Zielgruppe:
Die Zielgruppe für die Autobeklebung umfasst Eltern, Familien und Frauen, die auf der Suche nach ganzheitlichen Gesundheitslösungen sind. Dies schließt sowohl Menschen ein, die nach Kursen und Gemeinschaft suchen (sonnenfunken), als auch solche, die Interesse an Darmtherapien haben (Heiter vital Petra Lohmann).
4. Ziele der Autobeklebung:
- Erhöhung der Sichtbarkeit und Bekanntheit der beiden Unternehmen
- Ansprache der Zielgruppe während des täglichen Verkehrs
- Vermittlung von Informationen über die angebotenen Dienstleistungen und Kurse
**5. Designvorschläge:**
- Die Beklebung sollte auffällig sein (bitte nicht zu bunt )und das Logo sowie die Kontaktdaten beider Unternehmen klar darstellen.
Aufgabenstellung
eyecather Kundengewinnung. (hatte schon an einen kackhaufen gedacht, aber das mag ich nicht). nicht zu bunt. ist ein grauer T7 (Pure Grey, Raven-Sandwick/Raven-Sandwick/Raven). . nur die Scheiben sollen beklebt werden, maximal etwas über die Scheiben. Seitenscheiben und Heckscheibe. Die Heckscheibe (hatte ich schonmal in Waben Folie Komplett. Von innen kann man raus schauen. Von außen nicht rein)

```html
<!DOCTYPE html>
<html lang="de">
<head>
<meta charset="utf-8">
<title>Fensterbeschriftung – Heiter vital & Sonnenfunken</title>
<link rel="stylesheet" href="https://fonts.googleapis.com/css2?family=Montserrat:wght@400;600&display=swap">
<style>
  :root {
    --page: #f2f3f3;
    --teal: #8ed2cf;
    --teal-light: #b7e4e1;
    --teal-deep: #6fbfbd;
    --lime: #c3cf3a;
    --lime-soft: #dfe38a;
    --white: #ffffff;
    --ink: #ffffff;
    --ink-soft: #f3fbfa;
  }
  * { margin: 0; padding: 0; box-sizing: border-box; }
  html, body { width: 1200px; height: 1200px; overflow: hidden; }
  body {
    background: var(--page);
    font-family: "Montserrat", sans-serif;
    display: flex;
    flex-direction: column;
    align-items: center;
    justify-content: center;
    gap: 90px;
  }
  .window-panel {
    position: relative;
    overflow: hidden;
    border-radius: 10px;
    background: linear-gradient(180deg, var(--teal-light) 0%, var(--teal) 60%, var(--teal-deep) 100%);
  }
  .leaf-pattern {
    position: absolute; inset: 0;
    background: radial-gradient(ellipse at 50% 40%, rgba(255,255,255,0.18), rgba(255,255,255,0) 70%);
  }
  .waves { position: absolute; left: 0; bottom: 0; width: 100%; }

  /* side window */
  .side-window { width: 1100px; height: 330px; }
  .brand-vital {
    position: absolute; left: 50px; top: 36px; width: 440px; color: var(--ink);
  }
  .brand-vital .brand-row { display: flex; align-items: center; gap: 14px; }
  .brand-dot { flex: none; width: 44px; height: 44px; border-radius: 50%; background: var(--white); }
  .brand-stack { display: flex; flex-direction: column; line-height: 1.1; }
  .brand-name-top { font-weight: 600; font-size: 20px; letter-spacing: 2px; text-transform: uppercase; }
  .brand-name-main { font-weight: 600; font-size: 32px; letter-spacing: 1px; text-transform: uppercase; }
  .brand-tagline { font-size: 15px; margin-top: 10px; margin-left: 58px; }
  .web-vital {
    position: absolute; left: 50px; top: 206px; font-size: 14px; color: var(--ink);
  }
  .clover-figure {
    position: absolute; left: 555px; top: 18px; width: 150px; height: 150px;
  }
  .brand-funken {
    position: absolute; right: 50px; top: 40px; text-align: left; color: var(--ink);
  }
  .brand-funken .brand-name { font-weight: 400; font-size: 32px; letter-spacing: 0.5px; }
  .brand-funken .sub { font-size: 16px; margin-top: 2px; margin-left: 150px; }
  .brand-funken .address { font-size: 13px; margin-top: 40px; line-height: 1.5; }
  .brand-funken .web { font-size: 13px; margin-top: 6px; }

  /* rear window */
  .rear-window { width: 820px; height: 330px; }
  .rear-headline {
    position: absolute; top: 46px; width: 100%; text-align: center;
    color: var(--ink); font-weight: 600; font-size: 30px;
  }
  .rear-subline {
    position: absolute; top: 98px; width: 100%; text-align: center;
    color: var(--ink-soft); font-size: 20px;
  }
</style>
</head>
<body>

<section class="window-panel side-window">
  <div class="leaf-pattern" role="img" aria-label="Dezentes Blättermuster im Hintergrund"></div>

  <div class="brand-vital">
    <div class="brand-row">
      <span class="brand-dot"></span>
      <span class="brand-stack">
        <span class="brand-name-top">Heiter vital</span>
        <span class="brand-name-main">Petra Lohmann</span>
      </span>
    </div>
    <p class="brand-tagline">Darmtherapie für Frauen, Mamas &amp; Kinder</p>
  </div>
  <p class="web-vital">https://www.heiter-vital-petra-lohmann.de</p>

  <svg class="clover-figure" viewBox="0 0 150 150" role="img" aria-label="Kleeblatt-Illustration mit Angeboten">
    <rect x="0" y="0" width="150" height="150" rx="40" fill="var(--white)" opacity="0.85"/>
  </svg>

  <div class="brand-funken">
    <p class="brand-name">sonnenfunken</p>
    <p class="sub">Die Kurspraxis</p>
    <p class="address">Talwiesenweg 48<br>Kelbach</p>
    <p class="web">https://www.sonnenfunken-kelbach.de</p>
  </div>

  <svg class="waves" viewBox="0 0 1100 110" preserveAspectRatio="none" height="110" aria-hidden="true">
    <path d="M0 40 C250 0 500 90 1100 20 L1100 110 L0 110 Z" fill="var(--lime)"/>
    <path d="M0 62 C300 20 600 105 1100 45 L1100 110 L0 110 Z" fill="var(--white)"/>
    <path d="M0 85 C320 55 650 115 1100 75 L1100 110 L0 110 Z" fill="var(--lime-soft)"/>
  </svg>
</section>

<section class="window-panel rear-window">
  <div class="leaf-pattern" role="img" aria-label="Kleine Kleeblätter und Blätter als Hintergrundmuster"></div>
  <h2 class="rear-headline">Kleeblätter gehören nur zu Sonnenfunken.</h2>
  <p class="rear-subline">Daher bei heiter vital bitte weg. Danke. !!</p>
  <svg class="waves" viewBox="0 0 820 120" preserveAspectRatio="none" height="120" aria-hidden="true">
    <path d="M0 45 C200 0 420 100 820 25 L820 120 L0 120 Z" fill="var(--lime)"/>
    <path d="M0 68 C230 25 460 110 820 50 L820 120 L0 120 Z" fill="var(--white)"/>
    <path d="M0 92 C250 62 500 120 820 82 L820 120 L0 120 Z" fill="var(--lime-soft)"/>
  </svg>
</section>

</body>
</html>
```